Master & Realtor Did you know

I am a realtor and also a Master in Korean Martial arts, I would like to specifically market to my Karate clientele and make them aware that I am a realtor for the last 12 years in addition to being a karate instructor. also the similarities between both jobs Integrity, perseverance ,dedication, etc... also I would like to use a photo of myself on the front of the postcard that shows me in uniform and my suite attire.or I am open to a different approachRobert Reynolds

Target Market(s)

MY Karate clients

Industry/Entity Type

Real Estate Agent

Requirements
Must have
• Bullet points on the back with description of both job similarities example..
• Integrity, perseverance, focus, determination , people skills, be able to finish what I have started with the anticipated outcome.
• 33 years in teaching Martial Arts, 12 years as a professional Realtor.
• Please feel free to use your own words in description

```html
<!DOCTYPE html>
<html lang="en">
<head>
<meta charset="utf-8">
<title>Dennis Whitcombe – Realtor &amp; Martial Arts Master Postcard</title>
<link rel="stylesheet" href="https://fonts.googleapis.com/css2?family=Roboto+Slab:wght@800;900&family=Roboto+Condensed:wght@400;700&display=swap">
<style>
  :root {
    --stage: #dcd8d1;
    --navy-deep: #1d1f2e;
    --navy-mid: #2b2f48;
    --ink: #2a2a2e;
    --muted-ink: #444;
    --name-grey: #cfd0d4;
    --body-light: #dcdde2;
    --yellow: #f7d417;
    --headline-navy: #28226c;
    --band-dark: #2b2659;
    --photo-light: #d7d8da;
    --photo-dark: #a9abaf;
    --white: #ffffff;
    --stamp: #b8b8b8;
  }
  * { box-sizing: border-box; margin: 0; padding: 0; }
  html, body { width: 1200px; height: 655px; overflow: hidden; }
  body {
    background: var(--stage);
    position: relative;
    font-family: "Roboto Condensed", "Arial Narrow", sans-serif;
    color: var(--ink);
  }

  /* ---------- Front of postcard ---------- */
  .postcard-front {
    position: absolute; left: 40px; top: 25px;
    width: 473px; height: 612px;
    background: var(--white);
    box-shadow: 0 2px 6px rgba(0,0,0,.25);
    overflow: hidden;
  }
  .front-story {
    position: absolute; left: 0; top: 0; width: 270px; height: 447px;
    background: linear-gradient(180deg, #1b1c24 0%, #262a40 45%, #2e3350 75%, #3a3f5c 100%);
    padding: 22px 0 0 27px;
  }
  .agent-name {
    font-family: "Roboto Slab", Georgia, serif;
    font-weight: 900;
    font-size: 37px; line-height: 38px;
    color: var(--name-grey);
    letter-spacing: .2px;
  }
  .roles { list-style: none; margin-top: 10px; }
  .roles li {
    color: var(--yellow);
    font-size: 19px; line-height: 24px;
  }
  .roles li::before { content: "❖"; margin-right: 7px; font-size: 16px; }
  .did-you-know {
    margin-top: 15px;
    color: var(--white);
    font-weight: 700; font-size: 14.5px;
  }
  .story-copy p {
    width: 238px;
    color: var(--body-light);
    font-size: 12.6px; line-height: 15px;
    margin-top: 4px;
  }
  .story-copy p + p { margin-top: 13px; }

  .front-brand {
    position: absolute; left: 0; top: 447px; width: 270px; height: 80px;
    background: var(--white);
    display: flex; align-items: center; gap: 12px;
    padding-left: 14px;
  }
  .brand-square { width: 32px; height: 32px; background: var(--muted-ink); flex: none; }
  .brand-name {
    font-size: 22px; line-height: 23px; font-weight: 400; color: var(--ink);
    text-align: right;
  }
  .front-contact {
    position: absolute; left: 0; top: 527px; width: 270px; height: 85px;
    background: var(--yellow);
    padding: 16px 0 0 20px;
    font-weight: 700; font-size: 14.5px; line-height: 17px; color: var(--ink);
  }
  .contact-line { display: flex; align-items: center; gap: 5px; }
  .contact-line svg { flex: none; }
  .contact-line.indent { padding-left: 17px; }

  .photo {
    position: absolute; left: 270px; width: 203px;
  }
  .photo-suit {
    top: 0; height: 300px;
    background: radial-gradient(ellipse at 50% 40%, var(--photo-light) 0%, #bfc0c3 70%, var(--photo-dark) 100%);
  }
  .photo-divider { position: absolute; left: 270px; top: 300px; width: 203px; height: 6px; background: var(--yellow); }
  .photo-uniform {
    top: 306px; height: 306px;
    background: radial-gradient(ellipse at 50% 45%, #dcdcde 0%, #c6c7ca 70%, #b0b1b5 100%);
  }
  .school-badge {
    position: absolute; left: 290px; top: 318px;
    width: 30px; height: 30px; border-radius: 50%;
    background: #2f5d9c;
  }

  /* ---------- Back of postcard ---------- */
  .postcard-back {
    position: absolute; left: 550px; top: 95px;
    width: 610px; height: 472px;
    background: var(--white);
    box-shadow: 0 2px 6px rgba(0,0,0,.25);
    overflow: hidden;
  }
  .back-shade {
    position: absolute; left: 0; top: 0; width: 320px; height: 387px;
    background: linear-gradient(90deg, #d5d6da 0%, #ebebee 55%, rgba(255,255,255,0) 100%);
  }
  .name-band {
    position: absolute; left: 0; top: 17px; width: 610px; height: 21px;
    background: linear-gradient(90deg, #ececef 0%, #d9d8e2 25%, #8c88aa 50%, var(--band-dark) 75%, var(--band-dark) 100%);
  }
  .back-name {
    position: absolute; left: 28px; top: 18px;
    font-family: "Roboto Condensed", "Arial Narrow", sans-serif;
    font-weight: 700; font-size: 17px; line-height: 20px; color: var(--ink);
  }
  .back-roles {
    position: absolute; left: 29px; top: 44px;
    font-size: 12.5px; color: var(--ink);
  }
  .traits-heading {
    position: absolute; left: 20px; top: 64px;
    font-weight: 700; font-size: 15.5px; line-height: 17px;
    color: var(--headline-navy);
  }
  .traits {
    position: absolute; left: 20px; top: 105px;
    list-style: none;
    font-size: 12.5px; line-height: 16.7px; color: var(--ink);
  }
  .traits li { padding-left: 12px; position: relative; }
  .traits li::before {
    content: ""; position: absolute; left: 0; top: 6px;
    width: 6px; height: 6px; border-radius: 50%; background: var(--ink);
  }
  .consultation {
    position: absolute; left: 40px; top: 320px; width: 220px;
    text-align: center; font-size: 12.5px; line-height: 15.5px;
  }
  .consultation .cta { font-weight: 700; font-size: 13px; }
  .consultation .phone {
    font-weight: 700; font-size: 14px; color: var(--headline-navy);
    display: inline-flex; align-items: center; gap: 3px;
  }
  .back-brand {
    position: absolute; left: 352px; top: 52px;
    display: flex; align-items: center; gap: 7px;
  }
  .back-brand .brand-square { width: 18px; height: 30px; }
  .back-brand .brand-name { font-size: 14px; line-height: 14px; }
  .stamp-box {
    position: absolute; left: 516px; top: 48px;
    width: 68px; height: 76px;
    border: 3px dashed var(--stamp);
  }
</style>
</head>
<body>

<section class="postcard-front" aria-label="Postcard front">
  <div class="front-story">
    <h1 class="agent-name">Dennis<br>Whitcombe</h1>
    <ul class="roles">
      <li>Realtor</li>
      <li>Korean Martial Arts Master</li>
    </ul>
    <h2 class="did-you-know">DID YOU KNOW THAT</h2>
    <div class="story-copy">
      <p>Dennis Whitcombe is known for his ability to creatively pull a real estate transaction together using unique marketing campaigns, effective negotiating and a win-win attitude.</p>
      <p>That he&nbsp; is passionate about helping clients navigate the path to achieving their goal. Dennis works with traditional buyers and sellers in the Bucks,Montgomery,Hunterdon, West Chester, Delaware County area and has a great deal ofexperience with first time buyers, investors, foreclosures and short sales.</p>
      <p>That Dennis holds a 5th Degree Black Belt in the Art of Tang Soo Do Master and has been teaching the Korean martial art for 33 years.</p>
    </div>
  </div>

  <div class="front-brand">
    <span class="brand-square"></span>
    <span class="brand-name">Harlow Pike<br>Real Estate</span>
  </div>

  <div class="front-contact">
    <div class="contact-line">
      <svg width="13" height="13" viewBox="0 0 16 16" aria-hidden="true"><circle cx="8" cy="8" r="7" fill="none" stroke="#2a2a2e" stroke-width="1.5"/><path d="M5.5 4.5l1.5 1.5-1 1c.6 1.3 1.6 2.3 2.9 2.9l1-1 1.6 1.5-1.2 1.1C7.8 11.3 4.7 8.2 4.5 5.7z" fill="#2a2a2e"/></svg>
      <span>555.010.200</span>
    </div>
    <div class="contact-line">
      <svg width="12" height="9" viewBox="0 0 12 9" aria-hidden="true"><rect x="0.5" y="0.5" width="11" height="8" fill="none" stroke="#2a2a2e"/><path d="M0.5 0.5L6 5l5.5-4.5" fill="none" stroke="#2a2a2e"/></svg>
      <span>email dennis@harlowpike.com</span>
    </div>
    <div class="contact-line indent"><span>riverbendkarate@mail.com</span></div>
  </div>

  <div class="photo photo-suit" role="img" aria-label="Portrait of the agent in a dark suit with arms crossed"></div>
  <div class="photo-divider"></div>
  <div class="photo photo-uniform" role="img" aria-label="Portrait of the agent in a black martial arts uniform holding his black belt"></div>
  <span class="school-badge" aria-hidden="true"></span>
</section>

<section class="postcard-back" aria-label="Postcard back">
  <div class="back-shade"></div>
  <div class="name-band"></div>
  <h2 class="back-name">Dennis Whitcombe</h2>
  <p class="back-roles">Real Estate Agent | Korean Martial Arts Instructor</p>
  <h3 class="traits-heading">Personality Traits of a Successful<br>Real Estate Agent and Martial Arts Teacher</h3>
  <ul class="traits">
    <li>Perseverance</li>
    <li>Patience</li>
    <li>Inquisitiveness</li>
    <li>Discipline</li>
    <li>Execution</li>
    <li>Integrity</li>
    <li>Perseverance</li>
    <li>Focus</li>
    <li>Determination</li>
    <li>People Skills</li>
    <li>Being able to finish what i have started<br>with the anticipated outcome</li>
  </ul>
  <div class="consultation">
    <p class="cta">Call or email for FREE consultation</p>
    <p class="phone">
      <svg width="13" height="13" viewBox="0 0 16 16" aria-hidden="true"><circle cx="8" cy="8" r="7" fill="none" stroke="#28226c" stroke-width="1.5"/><path d="M5.5 4.5l1.5 1.5-1 1c.6 1.3 1.6 2.3 2.9 2.9l1-1 1.6 1.5-1.2 1.1C7.8 11.3 4.7 8.2 4.5 5.7z" fill="#28226c"/></svg>
      555.010.200
    </p>
    <p>m email dennis@harlowpike.com</p>
    <p>riverbendkarate@mail.com</p>
  </div>
  <div class="back-brand">
    <span class="brand-square"></span>
    <span class="brand-name">Harlow Pike<br>Real Estate</span>
  </div>
  <div class="stamp-box" aria-label="Stamp area"></div>
</section>

</body>
</html>
```